E brochure for company overview

We need a brochure for a company overview that will be sent to potential new clients. We are uploading a file with all the content that needs to be included inside of the brochure. We need this content to be displayed in a professional, neat, and creative way. The file has a Spanish and English version so we need two versions of the brochure in each language. *This brochure will be viewed digitally and it will not be printed, thus it does not need a cover page*. We included our company logo (Calvenor) Please utilize this in your design.

```html
<!DOCTYPE html>
<html lang="en">
<head>
<meta charset="utf-8">
<title>Calvenor – Company Overview</title>
<link rel="stylesheet" href="https://fonts.googleapis.com/css2?family=Barlow:wght@400;500;600&family=Barlow+Semi+Condensed:wght@600;700&family=Exo+2:wght@700&family=Poppins:wght@600&display=swap">
<style>
  :root{
    --backdrop:#1a1aad;
    --red:#d92b31;
    --black:#0b0b0b;
    --ink:#1c1c1c;
    --white:#ffffff;
    --photo-light:#e8edf6;
    --photo-mid:#b9c6dc;
    --photo-dark:#6d7e9c;
  }
  *{margin:0;padding:0;box-sizing:border-box}
  html,body{width:1200px;height:857px;overflow:hidden;background:var(--backdrop)}
  .canvas{position:relative;width:1200px;height:857px}
  .sheet{position:absolute;top:76px;width:498px;height:704px;background:var(--white);overflow:hidden;
    box-shadow:4px 4px 8px rgba(0,0,0,.35);font-family:"Barlow",sans-serif;color:var(--ink)}
  .sheet--en{left:77px}
  .sheet--es{left:616px}
  .hero{position:absolute;left:0;top:0}
  .brand{position:absolute;left:24px;top:28px;display:flex;align-items:center;gap:9px}
  .brand__dot{width:44px;height:44px;border-radius:50%;background:var(--red)}
  .brand__name{font-family:"Exo 2",sans-serif;font-weight:700;font-size:25px;line-height:1;color:var(--ink);letter-spacing:.5px}
  .brand__tag{font-family:"Barlow",sans-serif;font-size:9.6px;letter-spacing:.9px;color:var(--ink);margin-top:5px}
  .intro{position:absolute;left:24px;top:152px;width:210px;color:var(--white)}
  .intro__title{font-family:"Barlow Semi Condensed",sans-serif;font-weight:700;font-size:23px;letter-spacing:.3px;margin-bottom:8px}
  .intro__text{font-size:10.6px;line-height:15.9px}
  .history{position:absolute;left:19px;top:340px;width:465px}
  .history__lead{font-size:13.5px;margin-bottom:8px}
  .label{font-family:"Barlow Semi Condensed",sans-serif;font-weight:700;color:var(--red);font-size:15px}
  .history__text{font-size:13.4px;line-height:15.2px}
  .block{position:absolute;left:19px;width:208px}
  .block--mission{top:420px}
  .block--vision{top:512px}
  .block .label{display:block;margin-bottom:6px}
  .block__text{font-size:10px;line-height:13.4px;text-align:justify;font-weight:500}
  .services{position:absolute;left:258px;top:411px;width:225px;height:198px;border-left:1.5px solid var(--red)}
  .services__tab{position:absolute;left:-1.5px;top:0;height:25px;padding:0 14px 0 13px;background:var(--red);color:var(--white);
    font-family:"Barlow Semi Condensed",sans-serif;font-weight:700;font-size:14.5px;line-height:25px;border-radius:0 13px 13px 0}
  .services__text{position:absolute;left:13px;top:37px;width:208px;font-size:8.4px;line-height:13.4px;font-weight:500;text-align:justify}
  .values{position:absolute;left:14px;top:83px;list-style:none}
  .values li{display:flex;align-items:center;height:24.5px;font-family:"Barlow Semi Condensed",sans-serif;font-weight:600;font-size:10.6px;letter-spacing:.3px}
  .values__icon{width:17px;height:17px;margin-right:12px;flex:none}
  .partners{position:absolute;left:0;top:630px;width:498px;height:74px;background:linear-gradient(90deg,#161616,var(--black))}
  .partners__title{position:absolute;left:29px;top:24px;font-family:"Poppins",sans-serif;font-weight:600;font-size:19px;color:var(--white)}
  .partners__pill{position:absolute;left:184px;top:9px;width:302px;height:56px;border-radius:28px;background:var(--white);
    border-right:3px solid var(--red);border-top:1.5px solid var(--red);border-bottom:1.5px solid var(--red);
    display:flex;align-items:center;justify-content:space-around;padding:0 14px}
  .partner{font-family:"Barlow",sans-serif;font-weight:600;font-size:11.5px;color:var(--ink);display:flex;align-items:center;gap:4px}
  .partner__mark{width:10px;height:10px;border-radius:50%;background:var(--red)}
</style>
</head>
<body>
<div class="canvas">

  <!-- English edition -->
  <section class="sheet sheet--en">
    <svg class="hero" width="498" height="360" viewBox="0 0 498 360">
      <rect x="0" y="92" width="300" height="210" fill="var(--black)"/>
      <path d="M99 102 H330 V292 H99 A95 95 0 0 1 99 102 Z" fill="var(--red)"/>
      <defs>
        <linearGradient id="photoEn" x1="0" y1="0" x2="1" y2="1">
          <stop offset="0" stop-color="var(--photo-light)"/>
          <stop offset=".55" stop-color="var(--photo-mid)"/>
          <stop offset="1" stop-color="var(--photo-dark)"/>
        </linearGradient>
      </defs>
      <ellipse cx="470" cy="120" rx="251" ry="231" fill="var(--white)"/>
      <ellipse cx="470" cy="120" rx="245" ry="225" fill="url(#photoEn)" role="img" aria-label="Photo of hands holding pens while reviewing a printed document"/>
    </svg>
    <div class="brand">
      <span class="brand__dot"></span>
      <div><div class="brand__name">CALVENOR</div><div class="brand__tag">IT CONSULTING AND SERVICES</div></div>
    </div>
    <div class="intro">
      <h2 class="intro__title">INSTRUCTIONS:</h2>
      <p class="intro__text">Construct a brief using this information. The brief will be sent to potential new clients to make them interested in following up with us and potential meetings.</p>
    </div>
    <div class="history">
      <p class="history__lead"><span class="label">HISTORY:</span> Calvenor initiates on 2006</p>
      <p class="history__text">Calvenor has 15 years in the technology industry , specialising in security management, infrastructure and service management.</p>
    </div>
    <div class="block block--mission">
      <span class="label">MISSION:</span>
      <p class="block__text">Providing our customers with the best human and technological resources with the clear objective of providing effective solutions using best industry practices .</p>
    </div>
    <div class="block block--vision">
      <span class="label">VISION:</span>
      <p class="block__text">To be recognized by our customers as an important company in the Dominican Republic in the area of security and infrastructure and achieve presence throughout the Caribbean and Central America.</p>
    </div>
    <div class="services">
      <div class="services__tab">OUR SERVICES:</div>
      <p class="services__text">Service Management, Security of information, Custom development, Device and network monitoring ,Devops, API management, StaffingValues</p>
      <ul class="values">
        <li><svg class="values__icon" viewBox="0 0 17 17"><circle cx="8.5" cy="8.5" r="8.5" fill="var(--red)"/><path d="M4 9 L7 11 L13 6" stroke="#fff" stroke-width="1.2" fill="none"/></svg>INTEGRITY</li>
        <li><svg class="values__icon" viewBox="0 0 17 17"><circle cx="8.5" cy="8.5" r="8.5" fill="var(--red)"/><circle cx="8.5" cy="7.5" r="3" stroke="#fff" fill="none"/><path d="M7 11.5 H10" stroke="#fff"/></svg>CREATIVITY</li>
        <li><svg class="values__icon" viewBox="0 0 17 17"><circle cx="8.5" cy="8.5" r="8.5" fill="var(--red)"/><rect x="5" y="5" width="7" height="7" stroke="#fff" fill="none"/></svg>TEAM WORK</li>
        <li><svg class="values__icon" viewBox="0 0 17 17"><circle cx="8.5" cy="8.5" r="8.5" fill="var(--red)"/><circle cx="8.5" cy="8.5" r="3.5" stroke="#fff" fill="none"/></svg>POSITIVE ATTITUDE</li>
        <li><svg class="values__icon" viewBox="0 0 17 17"><circle cx="8.5" cy="8.5" r="8.5" fill="var(--red)"/><circle cx="8.5" cy="6.5" r="2" stroke="#fff" fill="none"/><path d="M5 12.5 Q8.5 8 12 12.5" stroke="#fff" fill="none"/></svg>COMMITMENT</li>
      </ul>
    </div>
    <div class="partners">
      <span class="partners__title">Our Partners:</span>
      <div class="partners__pill">
        <span class="partner"><span class="partner__mark"></span>Brevalux</span>
        <span class="partner">Orvanta</span>
        <span class="partner">Taskmere</span>
        <span class="partner">Halpen</span>
      </div>
    </div>
  </section>

  <!-- Spanish edition -->
  <section class="sheet sheet--es" lang="es">
    <svg class="hero" width="498" height="360" viewBox="0 0 498 360">
      <rect x="0" y="92" width="300" height="210" fill="var(--black)"/>
      <path d="M99 102 H330 V292 H99 A95 95 0 0 1 99 102 Z" fill="var(--red)"/>
      <defs>
        <linearGradient id="photoEs" x1="0" y1="0" x2="1" y2="1">
          <stop offset="0" stop-color="var(--photo-light)"/>
          <stop offset=".55" stop-color="var(--photo-mid)"/>
          <stop offset="1" stop-color="var(--photo-dark)"/>
        </linearGradient>
      </defs>
      <ellipse cx="470" cy="120" rx="251" ry="231" fill="var(--white)"/>
      <ellipse cx="470" cy="120" rx="245" ry="225" fill="url(#photoEs)" role="img" aria-label="Foto de manos con bolígrafos revisando un documento impreso"/>
    </svg>
    <div class="brand">
      <span class="brand__dot"></span>
      <div><div class="brand__name">CALVENOR</div><div class="brand__tag">IT CONSULTING AND SERVICES</div></div>
    </div>
    <div class="intro">
      <h2 class="intro__title">INSTRUCTIONS:</h2>
      <p class="intro__text">Construct a brief using this information. The brief will be sent to potential new clients to make them interested in following up with us and potential meetings.</p>
    </div>
    <div class="history">
      <p class="history__lead"><span class="label">HISTORIA:</span> Calvenor inicia en 2006</p>
      <p class="history__text">Calvenor tiene 15 años en la industria de la tecnología, especializándose en administración de seguridad, infraestructura y administración de servicios.</p>
    </div>
    <div class="block block--mission">
      <span class="label">MISIÓN:</span>
      <p class="block__text">Brindar a nuestros clientes los mejores recursos humanos y tecnológicos con el claro objetivo de brindar soluciones efectivas utilizando las mejores prácticas de la industria.</p>
    </div>
    <div class="block block--vision">
      <span class="label">VISIÓN:</span>
      <p class="block__text">Ser reconocidos por nuestros clientes como una empresa importante en República Dominicana en el área de seguridad e infraestructura y lograr presencia en todo el Caribe y Centroamérica.</p>
    </div>
    <div class="services">
      <div class="services__tab">NUESTROS SERVICIOS:</div>
      <p class="services__text">Gestión de servicios, Seguridad de la información, Desarrollo personalizado, Monitorización de dispositivos y redes, Devops, Gestión de API, Staffing</p>
      <ul class="values">
        <li><svg class="values__icon" viewBox="0 0 17 17"><circle cx="8.5" cy="8.5" r="8.5" fill="var(--red)"/><path d="M4 9 L7 11 L13 6" stroke="#fff" stroke-width="1.2" fill="none"/></svg>INTEGRITY</li>
        <li><svg class="values__icon" viewBox="0 0 17 17"><circle cx="8.5" cy="8.5" r="8.5" fill="var(--red)"/><circle cx="8.5" cy="7.5" r="3" stroke="#fff" fill="none"/><path d="M7 11.5 H10" stroke="#fff"/></svg>CREATIVITY</li>
        <li><svg class="values__icon" viewBox="0 0 17 17"><circle cx="8.5" cy="8.5" r="8.5" fill="var(--red)"/><rect x="5" y="5" width="7" height="7" stroke="#fff" fill="none"/></svg>TEAM WORK</li>
        <li><svg class="values__icon" viewBox="0 0 17 17"><circle cx="8.5" cy="8.5" r="8.5" fill="var(--red)"/><circle cx="8.5" cy="8.5" r="3.5" stroke="#fff" fill="none"/></svg>POSITIVE ATTITUDE</li>
        <li><svg class="values__icon" viewBox="0 0 17 17"><circle cx="8.5" cy="8.5" r="8.5" fill="var(--red)"/><circle cx="8.5" cy="6.5" r="2" stroke="#fff" fill="none"/><path d="M5 12.5 Q8.5 8 12 12.5" stroke="#fff" fill="none"/></svg>COMMITMENT</li>
      </ul>
    </div>
    <div class="partners">
      <span class="partners__title">Our Partners:</span>
      <div class="partners__pill">
        <span class="partner"><span class="partner__mark"></span>Brevalux</span>
        <span class="partner">Orvanta</span>
        <span class="partner">Taskmere</span>
        <span class="partner">Halpen</span>
      </div>
    </div>
  </section>

</div>
</body>
</html>
```